Business card for Cat Cafe

I have started a small business and need a business card designed. The business is a cat cafe, that is, an ordinary cafe that serves coffee and snacks but with a twist - you can bring your cat to play. In fact the idea is to encourage everyone to come and bring your feline friend in order to build community and provide some fun and connections between fellow cat lovers. Themes of the business include;

- Fun
- Discovery
- Connections

The name of the cafe is Plates and Purrs!

We look forward to seeing what creative ideas you may have!
Updates

Hi,

 Please note the contact details as below;
7 Birch Lane, Maple Grove,
Harbourview, EVS
2999

Target Market(s)

Cat owners, any age group

Industry/Entity Type

Small Business

Requirements
Must have
• Must include some type of imagery of a cat itself.

```html
<!DOCTYPE html>
<html lang="en">
<head>
<meta charset="utf-8">
<title>Plates and Purrs! – Business Card</title>
<link rel="stylesheet" href="https://fonts.googleapis.com/css2?family=Archivo+Black&display=swap">
<style>
  :root {
    --backdrop: #cfcfcf;
    --card-white: #ffffff;
    --cafe-red: #b01e24;
    --cafe-red-deep: #9c1a1f;
    --swoosh-orange: #eb8a1c;
    --swoosh-gold: #f3a51f;
    --name-red: #a51c24;
    --cat-orange: #f08a1a;
    --cat-yellow: #f7c22a;
    --address-white: #ffffff;
  }
  * { margin: 0; padding: 0; box-sizing: border-box; }
  html, body {
    width: 1200px;
    height: 900px;
    overflow: hidden;
    background: var(--backdrop);
  }
  .canvas {
    position: relative;
    width: 1200px;
    height: 900px;
  }
  .business-card {
    position: absolute;
    left: 160px;
    top: 190px;
    width: 880px;
    height: 520px;
    border-radius: 34px;
    overflow: hidden;
    background: var(--card-white);
  }
  .card-swoosh {
    position: absolute;
    inset: 0;
    width: 880px;
    height: 520px;
  }
  .cafe-name {
    position: absolute;
    left: 56px;
    top: 48px;
    font-family: "Archivo Black", sans-serif;
    font-weight: 400;
    font-size: 58px;
    line-height: 1.05;
    color: var(--name-red);
  }
  .mascot-artwork {
    position: absolute;
    left: 320px;
    top: 60px;
    width: 250px;
    height: 250px;
    border-radius: 28px;
    background: radial-gradient(circle at 45% 40%, var(--cat-yellow), var(--cat-orange));
  }
  .cafe-address {
    position: absolute;
    right: 34px;
    top: 390px;
    text-align: right;
    font-family: "Archivo Black", sans-serif;
    font-style: normal;
    font-weight: 400;
    font-size: 24px;
    line-height: 1.4;
    color: var(--address-white);
  }
</style>
</head>
<body>
  <main class="canvas">
    <section class="business-card">
      <svg class="card-swoosh" viewBox="0 0 880 520" aria-hidden="true">
        <defs>
          <linearGradient id="redBand" x1="0" y1="0" x2="1" y2="1">
            <stop offset="0" stop-color="#b01e24"/>
            <stop offset="1" stop-color="#9c1a1f"/>
          </linearGradient>
          <linearGradient id="orangeBand" x1="0" y1="1" x2="1" y2="0">
            <stop offset="0" stop-color="#f3a51f"/>
            <stop offset="1" stop-color="#eb8a1c"/>
          </linearGradient>
        </defs>
        <path d="M470,345 C660,315 800,250 880,125 L880,175 C800,270 660,325 470,345 Z" fill="url(#orangeBand)"/>
        <path d="M0,480 C220,380 560,360 880,190 L880,520 L0,520 Z" fill="url(#redBand)"/>
      </svg>

      <div class="mascot-artwork" role="img" aria-label="Cartoon tabby cat mascot holding a tray with a burger, fries and a drink"></div>

      <h1 class="cafe-name">Plates<br>and<br>Purrs!</h1>

      <address class="cafe-address">
        7 Birch Lane, Maple Grove,<br>
        Harbourview, EVS<br>
        2999
      </address>
    </section>
  </main>
</body>
</html>
```